Bellmoor Venues search & compare

We need a web design for a website (mobile & pc) which allows for searching and comparing of wedding locations. The design should be clean, stylish and original and it should have the following functionality:
- a search function (with summary overview and map view)
- a comparing function
- detail page per location
- review possibility
- login for storing favorites and show own history
- social function (liking, sharing, send to and cavorting)
- ad placement
- contact form

We also require a Logo Design. Please submit your ideas for that project here: Logo Design needed for web design project.

Wedding

```html
<!DOCTYPE html>
<html lang="en">
<head>
<meta charset="utf-8">
<title>Bellmoor Venues – Compare &amp; Search</title>
<link href="https://fonts.googleapis.com/css2?family=Quicksand:wght@300;400;500;600&display=swap" rel="stylesheet">
<style>
:root{
  --lavender:#f3def9;
  --lavender-2:#efd6f6;
  --purple:#9545b9;
  --purple-deep:#7a3199;
  --purple-dark:#6e2c8e;
  --violet-text:#b04dc8;
  --plum:#6a2a80;
  --brown:#5e4a3b;
  --ink:#3c3040;
  --gold:#f6c63a;
  --footer:#4a4a4a;
  --white:#ffffff;
}
*{margin:0;padding:0;box-sizing:border-box}
html,body{width:797px;height:1200px;overflow:hidden}
body{font-family:"Quicksand",sans-serif;color:var(--ink);background:var(--white);position:relative}
.abs{position:absolute}

.site-header{left:0;top:0;width:797px;height:77px;background:var(--lavender)}
.brand{left:90px;top:14px;display:flex;align-items:center;gap:8px}
.brand-dot{width:22px;height:22px;border-radius:50%;background:var(--purple)}
.brand-name{font-size:27px;font-weight:400;color:var(--violet-text);line-height:1}
.brand-tag{left:149px;top:46px;font-size:10px;color:#7a5a86}
.phone{left:511px;top:24px;font-size:17px;color:var(--violet-text)}

.hero-band{left:0;top:77px;width:797px;height:377px;background:var(--purple)}
.main-nav{left:69px;top:72px;width:661px;height:32px;background:var(--lavender);display:flex;align-items:center}
.main-nav a{font-size:12px;color:var(--ink);text-decoration:none;margin-right:23px}
.main-nav a.active{background:var(--brown);color:#f0e6dc;height:29px;line-height:29px;padding:0 10px;margin-left:1px;margin-right:16px}
.share{left:531px;top:79px;display:flex;gap:6px;align-items:center}
.share-btn{height:13px;width:32px;background:#8a7aa6;border-radius:2px}
.share-btn.tw{background:#9cc8e6}
.share-btn.gp{background:#e8e0ea;width:20px}
.share-count{font-size:7px;border:1px solid #ccc;background:#fff;padding:1px 3px;color:#555;margin-right:8px}

.hero-frame{left:66px;top:114px;width:665px;height:304px;background:#e4d0ec;padding:4px}
.hero-photo{width:100%;height:100%;background:linear-gradient(135deg,#d8d3ce 0%,#f2efe9 40%,#cfc3b5 70%,#e8e3dc 100%)}
.hero-caption{left:177px;top:360px;width:467px;height:41px;background:var(--purple);color:var(--white);font-size:26px;font-weight:300;text-align:center;line-height:41px}
.hero-caption em{font-style:normal;color:var(--gold)}
.slider-dots{left:356px;top:428px;width:85px;height:26px;background:var(--purple-deep);border-radius:4px 4px 0 0;display:flex;justify-content:center;align-items:center;gap:6px}
.slider-dots span{width:8px;height:8px;border-radius:50%;background:var(--white)}

.finder{left:0;top:454px;width:797px;height:182px;background:linear-gradient(90deg,#ecd0f5,#f2dcf8 50%,#ecd0f5)}
.finder-title{left:0;top:492px;width:797px;text-align:center;font-size:30px;font-weight:300;color:var(--ink)}
.finder-sub{left:0;top:533px;width:797px;text-align:center;font-size:17px;font-weight:400;color:var(--ink)}
.search-bar{left:74px;top:565px;width:603px;height:53px;background:var(--purple)}
.field{background:var(--white);font-size:12px;height:31px;line-height:31px;padding:0 8px;color:var(--ink)}
.select{left:83px;top:576px;width:227px}
.select svg{position:absolute;right:10px;top:12px}
.near{left:317px;top:576px;width:227px;color:#aaa}
.find-btn{left:549px;top:576px;width:119px;height:31px;background:var(--purple-deep);color:#f3e4f9;font-size:13px;text-align:center;line-height:31px}

.gallery-title{left:0;top:647px;width:797px;text-align:center;font-size:31px;font-weight:300;color:var(--plum)}
.gallery-band{left:0;top:750px;width:797px;height:175px;background:var(--lavender)}
.gallery-panel{left:81px;top:696px;width:627px;height:54px;background:var(--lavender)}
.card-label{font-size:13px;line-height:14px;color:var(--ink);top:712px;width:130px}
.card-img{top:750px;width:130px;height:135px}
.arrow{top:896px;width:21px;height:21px;border-radius:50%;background:var(--purple)}
.arrow svg{display:block;margin:5px auto}

.contact{left:0;top:930px;width:797px;height:193px;background:var(--purple)}
.contact-title{left:88px;top:942px;font-size:28px;font-weight:300;color:var(--white)}
.input{background:#eeeaf0;border-radius:3px;font-size:9px;color:#444;padding:7px 10px}
.submit{left:492px;top:1030px;width:102px;height:49px;background:var(--purple-dark);border-radius:3px;color:var(--white);font-size:13px;font-weight:600;text-align:center;line-height:49px}

.site-footer{left:0;top:1123px;width:797px;height:77px;background:var(--footer)}
.footer-nav{left:0;top:1142px;width:797px;display:flex;justify-content:center;gap:22px}
.footer-nav a{font-size:12px;color:#ddd;text-decoration:none}
.copyright{left:0;top:1174px;width:797px;text-align:center;font-size:8px;color:#eee}
</style>
</head>
<body>

<header class="site-header abs"></header>
<div class="brand abs"><span class="brand-dot"></span><span class="brand-name">Bellmoor Venues</span></div>
<div class="brand-tag abs">Compare &amp; Search</div>
<div class="phone abs">Call Us : 1800 . 420 .7716</div>

<div class="hero-band abs"></div>
<nav class="main-nav abs">
  <a class="active" href="#">Home</a>
  <a href="#">Wedding Venues</a>
  <a href="#">Wedding Ideas</a>
  <a href="#">Offer</a>
  <a href="#">Events</a>
  <a href="#">My Venues</a>
</nav>
<div class="share abs">
  <span class="share-btn"></span><span class="share-count">112</span>
  <span class="share-btn tw"></span><span class="share-count">9</span>
  <span class="share-btn gp"></span><span class="share-count">13</span>
</div>

<div class="hero-frame abs"><div class="hero-photo" role="img" aria-label="Table setting with a yellow flower, brown ribbon and a tealight candle"></div></div>
<div class="hero-caption abs">Need <em>INSPIRATION</em> For Your Big Day</div>
<div class="slider-dots abs"><span></span><span></span><span></span><span></span><span></span></div>

<section class="finder abs" role="img" aria-label="Faint city street map background"></section>
<h1 class="finder-title abs">FIND YOUR VENUE</h1>
<p class="finder-sub abs">with the most trusted resource for wedding reviews</p>
<div class="search-bar abs"></div>
<div class="field select abs">Ceremony &amp; Reception Venu
  <svg width="12" height="7" viewBox="0 0 12 7"><path d="M1 1l5 5 5-5" fill="none" stroke="#9545b9" stroke-width="1.3"/></svg>
</div>
<div class="field near abs">Near</div>
<div class="find-btn abs">Find a Vendors</div>

<h2 class="gallery-title abs">Wedding Inspiration Gallery</h2>
<div class="gallery-band abs"></div>
<div class="gallery-panel abs"></div>
<div class="card-label abs" style="left:95px">Indoor Ceremony<br>Venues</div>
<div class="card-label abs" style="left:253px">Outdoor Ceremony<br>Venues</div>
<div class="card-label abs" style="left:415px">Indoor Reception<br>Venues</div>
<div class="card-label abs" style="left:572px">Outdoor Reception<br>Venues</div>
<div class="card-img abs" style="left:97px;background:linear-gradient(160deg,#2e3a4e,#4a5668 60%,#2a3140)" role="img" aria-label="Couple embracing on a tiled floor"></div>
<div class="card-img abs" style="left:254px;background:linear-gradient(180deg,#1e2a4a,#6a4a3a 55%,#b05a3a)" role="img" aria-label="Outdoor dinner tables lit at night"></div>
<div class="card-img abs" style="left:411px;background:linear-gradient(180deg,#c84a5a,#e8b0b8 45%,#7a6a5a)" role="img" aria-label="Aisle lined with tall flower arrangements"></div>
<div class="card-img abs" style="left:566px;background:linear-gradient(180deg,#dfe4e6,#f3f1ee 50%,#e6e0d8)" role="img" aria-label="Reception table set with glassware and flowers"></div>
<div class="arrow abs" style="left:374px"><svg width="7" height="11" viewBox="0 0 7 11"><path d="M6 1L1.5 5.5 6 10" fill="none" stroke="#fff" stroke-width="1.3"/></svg></div>
<div class="arrow abs" style="left:401px"><svg width="7" height="11" viewBox="0 0 7 11"><path d="M1 1l4.5 4.5L1 10" fill="none" stroke="#fff" stroke-width="1.3"/></svg></div>

<section class="contact abs"></section>
<h2 class="contact-title abs">Contact Us</h2>
<div class="input abs" style="left:89px;top:989px;width:190px;height:27px">Name</div>
<div class="input abs" style="left:289px;top:989px;width:190px;height:27px">Email Id</div>
<div class="input abs" style="left:489px;top:988px;width:190px;height:27px">Phone</div>
<div class="input abs" style="left:89px;top:1028px;width:390px;height:53px">Message</div>
<div class="submit abs">Submit</div>

<footer class="site-footer abs"></footer>
<nav class="footer-nav abs">
  <a href="#">Home</a><a href="#">Wedding Venues</a><a href="#">Wedding Ideas</a><a href="#">Offer</a><a href="#">Events</a><a href="#">My Venues</a>
</nav>
<div class="copyright abs">© 2014.www.bellmoorvenues.com</div>

</body>
</html>
```